verdant terraces simple classy business card design

my name is owen harlow and I run a gardening business aimed at high class verdant terraces. the business name is verdant terraces and our logo was designed on pixel forum .My clientel are anything from residential homes to businesses. I take pride in my work and know that I offer a service like no other in my area.
The business card will be used to represent my business and I want it to be not only rememberable, but simplistic and modern. Eye catching too. Of course I would like it relatable to gardening and appealing to the correct clientel - those being garden enthusiasts, prestigious homes and businesses that are after top of the line gardening services like no other on the market.
I am not a typical lawn mowing business so I don't want a typical card design that represents that. The gardens I work with are generally million dollar properties with owners who are very garden proud looking for upkeep and guidance from me along with sometimes whole new garden designs. I want the business cards to show to my clients that I take pride, as they do, in their garden. And I want them to know from my card that I am a professional, qualified horticulturist offering them a top of the line service for life. I want them to refer my business on. I want them to look at my business card and see class and professionalism in a modern unique bold way.
The card should be simple with the possibility of the logo on the front being embossed/debossed and my details on the back the card should have a organic garden feel it's very important to me that it is absolutely perfect
I am also very open to ideas and suggestions so look forward to seeing the designs. the business logo has been supplied with this project and I want the card to be double sided

Contact info is
Owen Harlow - Managing Director / Horticulturist
Phone : 0481 526 704
Email: owenharlow@verdantterraces.com.au

Target Market(s)

high class gardens residential and commercial

Industry/Entity Type

Gardener

Contact Information for Business Card

Contact info is
Phone : 0481 526 704

PLEASE MAKE CARD DOUBLE SIDED

Requirements
Must have
• organic simple classy modern feel
• must flow with the current logo that has been supplied with this project
• Double sided
• Must explain in a simple way that I deal with high end gardens and I'm a qualified horticulturist
Nice to have
• embossed debossed logo
Should not have
• shouldn't be to busy or cheap looking

```html
<!DOCTYPE html>
<html lang="en">
<head>
<meta charset="utf-8">
<title>Verdant Terraces – Business Card</title>
<link rel="stylesheet" href="https://fonts.googleapis.com/css2?family=Cinzel:wght@400;600&family=Tinos:wght@400;700&display=swap">
<style>
  :root {
    --backdrop: #e9e6e1;
    --card-stock: #f2f2f1;
    --emboss-grey: #8d8d8d;
    --leaf-green: #5d9e4f;
    --ink: #2a2a2a;
  }
  * { margin: 0; padding: 0; box-sizing: border-box; }
  html, body { width: 1200px; height: 947px; overflow: hidden; }
  body {
    position: relative;
    background: var(--backdrop);
    font-family: "Tinos", "Times New Roman", serif;
  }
  .card {
    position: absolute;
    width: 437px;
    height: 720px;
    background: var(--card-stock);
    box-shadow: 0 2px 10px rgba(0,0,0,0.18);
  }
  .card--front { left: 133px; top: 113px; }
  .card--back  { left: 647px; top: 116px; }

  /* Front: debossed wordmark */
  .front-mark {
    position: absolute;
    left: 50%;
    top: 190px;
    transform: translateX(-50%);
    width: 230px;
    height: 230px;
    border-radius: 50%;
    background: #e4e4e3;
    box-shadow: inset 2px 2px 4px rgba(0,0,0,0.18), inset -2px -2px 3px rgba(255,255,255,0.8);
  }
  .front-name {
    position: absolute;
    left: 0; right: 0;
    top: 475px;
    text-align: center;
    font-family: "Cinzel", "Times New Roman", serif;
    font-weight: 400;
    font-size: 34px;
    line-height: 1.35;
    letter-spacing: 6px;
    color: var(--emboss-grey);
    text-transform: uppercase;
  }

  /* Back */
  .leaf-band {
    position: absolute;
    left: 4px; right: 4px; top: 4px;
    height: 62px;
    background: linear-gradient(180deg, var(--leaf-green) 0%, rgba(93,158,79,0.55) 70%, rgba(93,158,79,0) 100%);
  }
  .back-mark {
    position: absolute;
    left: 50%;
    top: 205px;
    transform: translateX(-50%);
    width: 62px; height: 62px;
    border-radius: 50%;
    background: var(--leaf-green);
  }
  .back-name {
    position: absolute;
    left: 0; right: 0;
    top: 282px;
    text-align: center;
    font-family: "Cinzel", "Times New Roman", serif;
    font-weight: 600;
    font-size: 28px;
    line-height: 1.3;
    letter-spacing: 3px;
    color: var(--leaf-green);
    text-transform: uppercase;
  }
  .holder-name {
    position: absolute;
    left: 0; right: 0; top: 412px;
    text-align: center;
    font-weight: 700;
    font-size: 25px;
    color: var(--leaf-green);
    text-transform: uppercase;
  }
  .holder-role {
    position: absolute;
    left: 0; right: 0; top: 444px;
    text-align: center;
    font-size: 20px;
    color: var(--ink);
    text-transform: uppercase;
  }
  .contact-icon {
    position: absolute;
    left: 50%;
    transform: translateX(-50%);
    fill: none;
    stroke: var(--leaf-green);
    stroke-width: 2;
  }
  .contact-icon--phone { top: 497px; }
  .contact-icon--mail { top: 580px; }
  .contact-line {
    position: absolute;
    left: 0; right: 0;
    text-align: center;
    font-size: 22px;
    color: var(--ink);
  }
  .contact-line--phone { top: 538px; }
  .contact-line--mail { top: 610px; }
</style>
</head>
<body>
  <section class="card card--front" aria-label="Card front">
    <div class="front-mark"></div>
    <p class="front-name">Verdant<br>Terraces</p>
  </section>

  <section class="card card--back" aria-label="Card back">
    <div class="leaf-band" role="img" aria-label="Row of scattered green leaves along the top edge"></div>
    <div class="back-mark"></div>
    <p class="back-name">Verdant<br>Terraces</p>
    <p class="holder-name">Owen Harlow</p>
    <p class="holder-role">Managing Director</p>
    <svg class="contact-icon contact-icon--phone" width="18" height="26" viewBox="0 0 18 26" aria-hidden="true">
      <rect x="1.5" y="1.5" width="15" height="23" rx="2"/>
      <line x1="7" y1="20.5" x2="11" y2="20.5"/>
    </svg>
    <p class="contact-line contact-line--phone">0481526704</p>
    <svg class="contact-icon contact-icon--mail" width="28" height="18" viewBox="0 0 28 18" aria-hidden="true">
      <rect x="1.5" y="1.5" width="25" height="15"/>
      <polyline points="1.5,1.5 14,11 26.5,1.5"/>
    </svg>
    <p class="contact-line contact-line--mail">owenharlow@verdantterraces.com.au</p>
  </section>
</body>
</html>
```